Plover Scrap Ireland

Hi There,

We are a biofuels company based in Ireland. We produce biodiesel from waste cooking oils from restaurants and biogas from food waste.

We are mainly a B2B company - essentially we take from collectors of these products and they aggregate for us.

We would like to start collections of our own for both waste cooking oil
and food waste from restaurants, hotels, hospitals and offices. We will pay for the waste oil (a main focus) and charge competitive rates for the food waste - all will go to renewable solutions.

Can you design a logo for this business? And then also can you provide a leaflet outline so we can send to businesses/ post on social media. Emphasis should be on the circular model of our business.
Updates

Target Market(s)

Restaurants and Businesses

Industry/Entity Type

Waste Collection

Colors
0094D4
00A9DD
6FCCEA
C7EBF8
E9F6FB
00AB8E
00BBA5
67D7C9
C6EFE9
E9F9F6
59FF00
82FF00
B8FF75
E3FFCB
F4FFEA
FFF300
FFF600
FEFA6F
FFFEC7
FFFEE8

Requirements
Nice to have
• Renewable Ideas, Circular Nature

```html
<!DOCTYPE html>
<html lang="en">
<head>
<meta charset="utf-8">
<title>Plover Scrap Ireland – Biodiesel Leaflet</title>
<link rel="stylesheet" href="https://fonts.googleapis.com/css2?family=Montserrat:wght@500;700;800&family=Lato:wght@300;400&display=swap">
<style>
  :root {
    --navy: #30358c;
    --green: #8bc53f;
    --yellow: #fddc17;
    --white: #ffffff;
    --stage: #eef2ee;
  }
  html, body {
    margin: 0;
    width: 1200px;
    height: 849px;
    overflow: hidden;
    background: var(--stage);
  }
  .leaflet-frame {
    position: absolute;
    left: 324px;
    top: 35px;
    width: 551px;
    height: 780px;
    box-shadow: 0 10px 30px rgba(0,0,0,0.18);
  }
  .leaflet {
    position: absolute;
    left: 0;
    top: 0;
    width: 970px;
    height: 1373px;
    transform: scale(0.568);
    transform-origin: 0 0;
    background: var(--white);
    overflow: hidden;
    font-family: "Montserrat", sans-serif;
  }
  .leaflet-shapes {
    position: absolute;
    inset: 0;
  }
  .brand {
    position: absolute;
    left: 75px;
    top: 62px;
    display: flex;
    align-items: center;
    gap: 16px;
    color: var(--white);
    font-weight: 700;
    font-size: 34px;
    letter-spacing: -0.5px;
  }
  .brand-dot {
    width: 46px;
    height: 46px;
    border-radius: 50%;
    background: var(--green);
  }
  .headline {
    position: absolute;
    left: 73px;
    top: 190px;
    margin: 0;
    color: var(--white);
    font-weight: 800;
    font-size: 80px;
    line-height: 0.92;
    letter-spacing: -3px;
  }
  .tagline {
    position: absolute;
    left: 80px;
    top: 436px;
    margin: 0;
    color: var(--white);
    font-weight: 500;
    font-size: 28px;
    line-height: 1.27;
  }
  .why-title {
    position: absolute;
    left: 163px;
    top: 628px;
    margin: 0;
    color: var(--white);
    font-weight: 800;
    font-size: 70px;
    line-height: 0.95;
    letter-spacing: -3px;
  }
  .reasons {
    position: absolute;
    left: 173px;
    top: 0;
    margin: 0;
    padding: 0;
    list-style: none;
    font-family: "Lato", sans-serif;
    font-weight: 300;
    font-size: 23.5px;
    line-height: 1.26;
    color: var(--white);
  }
  .reasons li {
    position: absolute;
    left: 0;
    width: 560px;
    transform: translateY(-50%);
  }
  .contact-title {
    position: absolute;
    left: 67px;
    top: 1256px;
    margin: 0;
    color: var(--white);
    font-weight: 800;
    font-size: 46px;
    line-height: 0.88;
    letter-spacing: -1.5px;
  }
  .contact-details {
    position: absolute;
    right: 89px;
    top: 1268px;
    margin: 0;
    text-align: right;
    color: var(--navy);
    font-weight: 500;
    font-size: 30px;
    line-height: 1.25;
    letter-spacing: -0.8px;
  }
  .contact-details strong { font-weight: 800; }
</style>
</head>
<body>
<div class="leaflet-frame">
  <main class="leaflet">
    <svg class="leaflet-shapes" viewBox="0 0 970 1373" width="970" height="1373" aria-hidden="true">
      <polygon points="0,573 731,573 970,925 970,1242 0,1242" fill="var(--green)"/>
      <polygon points="790,655 812,648 970,890 970,965" fill="var(--navy)"/>
      <polygon points="0,0 497,0 690,338 600,573 0,573" fill="var(--navy)"/>
      <polyline points="508,0 702,338 665,400" fill="none" stroke="var(--green)" stroke-width="14" stroke-linejoin="miter"/>
      <polygon points="0,1242 313,1242 232,1373 0,1373" fill="var(--navy)"/>
    </svg>

    <svg class="leaflet-shapes" viewBox="0 0 970 1373" width="970" height="1373" role="img" aria-label="Oil droplet in a hexagon badge">
      <polygon points="527,537 607,395 767,395 847,537 767,679 607,679" fill="var(--navy)" stroke="var(--green)" stroke-width="12" stroke-linejoin="round"/>
      <path d="M687,420 C700,470 757,540 757,590 C757,630 726,656 687,656 C648,656 617,630 617,590 C617,540 674,470 687,420 Z" fill="var(--yellow)"/>
    </svg>

    <svg class="leaflet-shapes" viewBox="0 0 970 1373" width="970" height="1373" aria-hidden="true">
      <g class="bullet-icons" fill="var(--navy)">
        <circle cx="106" cy="838" r="40"/>
        <circle cx="106" cy="936" r="40"/>
        <circle cx="106" cy="1034" r="40"/>
        <circle cx="106" cy="1132" r="40"/>
      </g>
      <g fill="var(--yellow)">
        <path d="M106,814 C109,826 118,840 118,848 C118,856 113,861 106,861 C99,861 94,856 94,848 C94,840 103,826 106,814 Z"/>
        <path d="M106,912 C109,924 118,938 118,946 C118,954 113,959 106,959 C99,959 94,954 94,946 C94,938 103,924 106,912 Z"/>
        <path d="M106,1010 C109,1022 118,1036 118,1044 C118,1052 113,1057 106,1057 C99,1057 94,1052 94,1044 C94,1036 103,1022 106,1010 Z"/>
        <path d="M106,1108 C109,1120 118,1134 118,1142 C118,1150 113,1155 106,1155 C99,1155 94,1150 94,1142 C94,1134 103,1120 106,1108 Z"/>
      </g>
    </svg>

    <div class="brand"><span class="brand-dot"></span><span>Plover Scrap Ireland</span></div>

    <h1 class="headline">We make<br>Biodiesel<br>from used oil.</h1>

    <p class="tagline">Recycling Used Oil<br>Recycling For The Better<br>and creating sustainability.</p>

    <h2 class="why-title">Why work<br>with us?</h2>

    <ul class="reasons">
      <li style="top:837px">We are a biofuels company based in Ireland.<br>We produce biodiesel from waste cooking oils from<br>restaurants and biogas from food waste.</li>
      <li style="top:933px">&nbsp;biodiesel from waste cooking oils from<br>restaurants and biogas from food waste.</li>
      <li style="top:1032px">waste cooking oils from<br>restaurants and biogas from food waste.</li>
      <li style="top:1133px">We are a biofuels company based in Ireland.</li>
    </ul>

    <h2 class="contact-title">Get in<br>Touch</h2>
    <p class="contact-details"><strong>Call us:</strong> +353 1 555 0142<br><strong>E-mail:</strong> hello@ploverscrapireland.com</p>
  </main>
</div>
</body>
</html>
```